Business Card Design Project

it should have the logo in one side
the other side

Name
Position
telephone
email

Target Market(s)

Business prospects and upscale Fashion shoppers

Industry/Entity Type

Business

Font styles to use
Serif
Sans Serif

Requirements
Must have
• very elegant, upscale, modern
Nice to have
• layering, embossed
Should not have
• Should not use any color OTHER THAN black, silver, white or purple

```html
<!DOCTYPE html>
<html lang="en">
<head>
<meta charset="utf-8">
<title>Velara — Business Card</title>
<link rel="stylesheet" href="https://fonts.googleapis.com/css2?family=Lato:wght@400;700&display=swap">
<style>
  :root {
    --stage: #e6e6e8;
    --paper: #ffffff;
    --paper-shade: #ececee;
    --ink: #1c1c1e;
    --charcoal: #2b2b2d;
    --charcoal-deep: #141415;
    --silver: #c9c9cd;
    --purple: #7b3fa6;
    --purple-soft: #9a68c0;
  }
  * { box-sizing: border-box; margin: 0; padding: 0; }
  html, body {
    width: 1200px; height: 900px; overflow: hidden;
    background: var(--stage);
    font-family: "Lato", Arial, sans-serif;
    color: var(--ink);
  }
  .sheet {
    position: relative; width: 1200px; height: 900px;
    display: flex; flex-direction: column; align-items: center; justify-content: center; gap: 40px;
  }
  .card {
    position: relative; width: 680px; height: 389px; overflow: hidden;
    background: linear-gradient(160deg, var(--paper) 0%, var(--paper-shade) 100%);
    box-shadow: 0 10px 26px rgba(0,0,0,.18), 0 2px 4px rgba(0,0,0,.12);
  }
  .card-art { position: absolute; inset: 0; width: 100%; height: 100%; }

  /* Brand mark */
  .brand { position: absolute; display: flex; align-items: center; gap: 14px; }
  .brand-dot { width: 34px; height: 34px; border-radius: 50%; background: var(--purple); }
  .brand-name { font-size: 44px; font-weight: 400; letter-spacing: 3px; color: var(--ink); line-height: 1; }

  /* Front */
  .card-front .brand { left: 50%; top: 104px; transform: translateX(-50%); }
  .front-band {
    position: absolute; left: 0; right: 0; bottom: 0; height: 108px;
    background: linear-gradient(180deg, var(--charcoal) 0%, var(--charcoal-deep) 100%);
    display: flex; justify-content: center; padding-top: 26px;
  }
  .front-web { display: flex; align-items: center; gap: 10px; color: #f2f2f2; font-size: 17px; letter-spacing: .5px; height: 22px; }
  .front-web .web-icon { width: 20px; height: 20px; }

  /* Back */
  .card-back .brand { left: 62px; top: 150px; }
  .card-back .brand-name { font-size: 38px; }
  .card-back .brand-dot { width: 28px; height: 28px; }
  .holder { position: absolute; right: 84px; top: 88px; text-align: right; }
  .holder-name { font-size: 27px; font-weight: 400; color: var(--ink); line-height: 1.1; }
  .holder-role { font-size: 14px; color: var(--ink); margin-top: 2px; }

  .contacts { position: absolute; left: 455px; top: 266px; list-style: none; }
  .contacts li { display: flex; align-items: center; gap: 12px; height: 24px; font-size: 15px; color: var(--ink); letter-spacing: .2px; white-space: nowrap; }
  .contact-icon { width: 18px; height: 18px; flex: none; }
</style>
</head>
<body>
<main class="sheet">

  <!-- Logo side -->
  <section class="card card-front" aria-label="Card front">
    <div class="brand">
      <span class="brand-dot"></span>
      <span class="brand-name">VELARA</span>
    </div>
    <div class="front-band">
      <p class="front-web">
        <svg class="web-icon" viewBox="0 0 20 20" aria-hidden="true">
          <circle cx="10" cy="10" r="9.5" fill="#f2f2f2"/>
          <circle cx="10" cy="10" r="5.5" fill="none" stroke="#2b2b2d" stroke-width="1.4"/>
          <path d="M4.5 10h11M10 4.5c-2.5 3-2.5 8 0 11M10 4.5c2.5 3 2.5 8 0 11" fill="none" stroke="#2b2b2d" stroke-width="1.1"/>
        </svg>
        www.velarahouse.com
      </p>
    </div>
  </section>

  <!-- Details side -->
  <section class="card card-back" aria-label="Card back">
    <svg class="card-art" viewBox="0 0 680 389" preserveAspectRatio="none" aria-hidden="true">
      <defs>
        <linearGradient id="bandShade" x1="0" y1="0" x2="0" y2="1">
          <stop offset="0" stop-color="#2b2b2d"/>
          <stop offset="1" stop-color="#141415"/>
        </linearGradient>
      </defs>
      <path d="M0 284 H360 L396 216 H680 V389 H0 Z" fill="url(#bandShade)"/>
      <path d="M680 258 H436 L408 312 L436 366 H680 Z" fill="#ffffff"/>
      <path d="M0 276 H355 L391 208 H680" fill="none" stroke="#7b3fa6" stroke-width="2.5"/>
    </svg>

    <div class="brand">
      <span class="brand-dot"></span>
      <span class="brand-name">VELARA</span>
    </div>

    <div class="holder">
      <p class="holder-name">Your Name</p>
      <p class="holder-role">Manager</p>
    </div>

    <ul class="contacts">
      <li>
        <svg class="contact-icon" viewBox="0 0 18 18" aria-hidden="true">
          <circle cx="9" cy="9" r="9" fill="#7b3fa6"/>
          <path d="M6 4.8c.5-.3 1-.2 1.3.3l.8 1.4c.2.4.1.8-.2 1.1l-.5.4c.5 1.1 1.3 1.9 2.4 2.4l.4-.5c.3-.3.7-.4 1.1-.2l1.4.8c.5.3.6.8.3 1.3-.6 1-1.6 1.4-2.6 1-2.3-.9-4-2.6-4.9-4.9-.4-1 0-2 .5-2.6z" fill="#fff"/>
        </svg>
        (555) 014 2290
      </li>
      <li>
        <svg class="contact-icon" viewBox="0 0 18 18" aria-hidden="true">
          <circle cx="9" cy="9" r="9" fill="#7b3fa6"/>
          <rect x="4.5" y="5.8" width="9" height="6.4" rx=".8" fill="none" stroke="#fff" stroke-width="1.2"/>
          <path d="M4.8 6.2 9 9.4l4.2-3.2" fill="none" stroke="#fff" stroke-width="1.2"/>
        </svg>
        hello@velarahouse.com
      </li>
      <li>
        <svg class="contact-icon" viewBox="0 0 18 18" aria-hidden="true">
          <circle cx="9" cy="9" r="9" fill="#7b3fa6"/>
        </svg>
        social.velarahouse.com
      </li>
      <li>
        <svg class="contact-icon" viewBox="0 0 18 18" aria-hidden="true">
          <circle cx="9" cy="9" r="9" fill="#7b3fa6"/>
          <circle cx="9" cy="9" r="4.6" fill="none" stroke="#fff" stroke-width="1.2"/>
          <path d="M4.4 9h9.2M9 4.4c-2 2.6-2 6.6 0 9.2M9 4.4c2 2.6 2 6.6 0 9.2" fill="none" stroke="#fff" stroke-width="1"/>
        </svg>
        www.velarahouse.com
      </li>
    </ul>
  </section>

</main>
</body>
</html>
```